Brightwave Reach - Business Card

We need a business card for a Social Media Marketing company that specializes in online marketing for small businesses in Canada using common Social Media platforms such as Pictora, Kinloop, Flickmo & Chirpo.

I have uploaded a copy of our logo which I would like utilized in the business card. We would like the business card to be modern yet classy design.

Our website is www.brightwavereach.ca

Industry/Entity Type

Marketing

Contact Information for Business Card

Email: info@brightwavereach.ca
Website: www.brightwavereach.ca
Telephone: 604-392-5108

Colors

Designer to choose colors to be used in the design.

Requirements
Must have
• Social Media icons on reverse
• Please add some designs with color.

```html
<!DOCTYPE html>
<html lang="en">
<head>
<meta charset="utf-8">
<title>Brightwave Reach - Business Card</title>
<link rel="stylesheet" href="https://fonts.googleapis.com/css2?family=Open+Sans:wght@400;600;700;800&display=swap">
<style>
  :root {
    --backdrop: #d9d9d9;
    --card: #ffffff;
    --ink: #3a3a3a;
    --ink-soft: #8a8a8a;
    --rule: #3a3a3a;
    --shadow: rgba(0, 0, 0, 0.28);
  }
  * { box-sizing: border-box; margin: 0; padding: 0; }
  html, body {
    width: 1200px;
    height: 1000px;
    overflow: hidden;
    background: var(--backdrop);
    font-family: "Open Sans", Arial, sans-serif;
    color: var(--ink);
  }
  .stage { position: relative; width: 1200px; height: 1000px; }
  .card {
    position: absolute;
    background: var(--card);
    box-shadow: 0 14px 30px var(--shadow);
  }
  .brand {
    position: absolute;
    display: flex; align-items: center; gap: 12px;
  }
  .brand__mark {
    flex: none;
    width: 22px; height: 22px;
    border: 3px solid var(--ink);
  }
  .brand__name {
    font-weight: 800;
    text-transform: uppercase;
    color: var(--ink);
    line-height: 1;
    text-align: center;
    letter-spacing: 0.5px;
  }
  .brand__name span { display: block; }

  /* Reverse side */
  .card--back { left: 430px; top: 60px; width: 660px; height: 377px; }
  .card--back .brand { left: 0; right: 0; top: 120px; justify-content: center; }
  .card--back .brand__name { font-size: 36px; }
  .social-list {
    position: absolute;
    left: 0; right: 0; bottom: 42px;
    display: flex; justify-content: center; gap: 14px;
    list-style: none;
    font-size: 12px; font-weight: 600;
    color: var(--ink);
  }

  /* Front side */
  .card--front { left: 110px; top: 500px; width: 780px; height: 446px; }
  .holder { position: absolute; left: 60px; top: 196px; }
  .holder__name {
    font-weight: 700; font-size: 30px; letter-spacing: 1.5px;
    text-transform: uppercase; color: var(--ink); line-height: 1.1;
  }
  .holder__title {
    font-weight: 600; font-size: 18px; color: var(--ink-soft);
    letter-spacing: 0.5px;
  }
  .holder__rule {
    width: 34px; height: 3px; background: var(--rule); margin-top: 12px;
  }
  .contact {
    position: absolute; left: 60px; top: 300px;
    list-style: none; font-size: 16px; line-height: 26px; color: var(--ink);
  }
  .card--front .brand { right: 50px; bottom: 60px; }
  .card--front .brand__name { font-size: 40px; }
</style>
</head>
<body>
<main class="stage">
  <section class="card card--back" aria-label="Business card reverse">
    <div class="brand">
      <span class="brand__mark"></span>
      <span class="brand__name"><span>Brightwave</span><span>Reach</span></span>
    </div>
    <ul class="social-list">
      <li>Kinloop</li>
      <li>Chirpo</li>
      <li>Pictora</li>
      <li>Flickmo</li>
    </ul>
  </section>

  <section class="card card--front" aria-label="Business card front">
    <div class="holder">
      <p class="holder__name">Daniel Brooks</p>
      <p class="holder__title">Precedent</p>
      <div class="holder__rule"></div>
    </div>
    <ul class="contact">
      <li>P: 604-392-5108</li>
      <li>E: info@brightwavereach.ca</li>
      <li>W: www.brightwavereach.ca</li>
    </ul>
    <div class="brand">
      <span class="brand__mark"></span>
      <span class="brand__name"><span>Brightwave</span><span>Reach</span></span>
    </div>
  </section>
</main>
</body>
</html>
```